A WEBSITE FOR A JEWELLERY RETAIL STORE WITH A SHOPPING CART, AND ABILITY TO ORDER ONLINE.

I require a website with a shopping cart.

We sell MAINLY diamond jewellery (such as rings etc). I need it to be simple to change prices with only a few buttons, as the price fluctuates due to the US Dollar.

We are a diamond wholesaler, selling directly to the public, so we guarantee the lowest prices in Australia.

There is also a link to current inventory that will need to be uploaded to the site.

This could be an ongoing job, where you will be paid weekly to maintain and update the website if you wish.

Target Market(s)

People getting engaged, and wanting to buy a diamond ring.

Number of Pages Required

5+ page

Colors

Designer to choose colors to be used in the design.

Requirements
Must have
• elegant.
• modern.
• professional.
• SHOPPING CART.
• ABILITY TO SEARCH FOR LOOSE DIAMONDS (LINK THAT NEEDS TO BE EMBEDDED WILL BE SENT WHICH SHOWS CURRENT STOCK).
• ENGAGEMENT RINGS
• WEDDING RINGS
• DIAMOND EARRINGS
• DIAMOND PENDANTS
• LOOSE DIAMONDS.
• SALE ITEMS.
• OTHER JEWELLERY.
• EDUCATION
• WISH LIST
• CART.
Nice to have
• a good place to look for inspiration on pages is https://www.lumenvael.example.
• YOU MAY VISIT OUR FACEBOOK PAGE AT.
• HTTP://WWW.SOCIALPAGE.EXAMPLE/QUILLSTONEJEWELLERS
Should not have
• We don't want it too busy.

```html
<!DOCTYPE html>
<html lang="en">
<head>
<meta charset="utf-8">
<title>Quillstone Jewellers — Home</title>
<link rel="stylesheet" href="https://fonts.googleapis.com/css2?family=Lato:wght@400;700&family=Merriweather:wght@700&display=swap">
<style>
:root{
  --stage:#d6d6d6;
  --black:#000;
  --ink:#111;
  --white:#fff;
  --gold:#f5c518;
  --grey-bar:#e4e4e4;
  --grey-dark:#3d3d3d;
  --grey-foot:#555;
  --muted:#bbb;
  --sans:'Lato',sans-serif;
  --serif:'Merriweather',serif;
}
*{box-sizing:border-box;margin:0;padding:0}
html,body{width:1200px;height:1200px;overflow:hidden;background:var(--stage)}
.page{position:absolute;left:455px;top:21px;width:290px;height:1158px;background:var(--white);overflow:hidden;font-family:var(--sans);color:var(--ink)}
.abs{position:absolute}
.btn{position:absolute;background:var(--gold);color:var(--white);border-radius:2px;font-size:4px;display:flex;align-items:center;justify-content:center;letter-spacing:.2px;white-space:nowrap}
.btn-outline{position:absolute;border:1px solid var(--white);color:var(--white);font-size:5px;display:flex;align-items:center;justify-content:center;border-radius:2px;white-space:nowrap}

/* top bar + nav */
.topbar{left:0;top:0;width:290px;height:13px;background:var(--grey-bar);font-size:3.6px;display:flex;align-items:center;padding:0 20px;gap:6px;white-space:nowrap}
.topbar .right{margin-left:auto;display:flex;gap:8px;align-items:center}
.nav{left:0;top:13px;width:290px;height:22px;background:var(--grey-bar);border-top:1px solid #d0d0d0}
.logo{left:32px;top:5px;display:flex;align-items:center;gap:3px;font-size:7px;letter-spacing:.3px;color:var(--ink)}
.logo .mark{width:6px;height:6px;background:var(--ink)}
.logo small{display:block;font-size:2.8px;letter-spacing:1.6px;margin-top:1px}
.menu{top:10px;font-size:3.6px;white-space:nowrap}
.menu.active{color:var(--gold)}
.dropdown{left:137px;top:30px;width:38px;background:var(--white);font-size:3.4px;text-align:center;box-shadow:0 1px 2px rgba(0,0,0,.3);white-space:nowrap}
.dropdown div{padding:1.6px 0}
.dropdown .on{background:var(--gold);color:var(--white)}

/* hero */
.hero{left:0;top:35px;width:290px;height:306px;background:radial-gradient(ellipse at 78% 35%,#7a6a55 0%,#3c342c 40%,#1b1714 100%)}
.hero-title{left:22px;top:72px;font-family:var(--serif);font-size:14px;color:var(--white)}
.hero-sub{left:22px;top:93px;font-size:3.6px;color:var(--white);line-height:1.3}
.cut{left:0;top:150px}
.tile{position:absolute;width:106px;height:96px}
.tile.black{background:var(--black);color:var(--white)}
.tile.photo{background:radial-gradient(circle,#f2f2f2 0%,#c9c9c9 45%,#fff 75%)}
.tile.photo.gold{background:radial-gradient(circle,#f5f0e0 0%,#d7c07a 40%,#fff 72%)}
.tile h3{position:absolute;left:14px;top:14px;font-size:5px;font-weight:400}
.tile p{position:absolute;left:14px;top:24px;width:70px;font-size:3.2px;line-height:1.3;color:#ddd}

/* sale band */
.sale{left:0;top:341px;width:290px;height:100px;background:var(--black);color:var(--white);text-align:center}
.sale .gem{left:74px;top:10px;width:76px;height:30px;background:linear-gradient(100deg,#2a2000,#9c7c10,#3a2d00);transform:rotate(-12deg);border-radius:40%}
.sale h2{position:absolute;left:0;right:0;top:30px;font-weight:400;font-size:12px;letter-spacing:.4px}
.sale .sub{position:absolute;left:0;right:0;top:48px;font-size:5px}

/* featured */
.section-h{font-size:7px;color:#333;white-space:nowrap}
.card{position:absolute;top:475px;width:58px;height:105px;border:1px solid #ccc;background:var(--white)}
.card.lift{box-shadow:0 1px 4px rgba(0,0,0,.4);border-color:#888}
.card .img{position:absolute;left:4px;top:4px;width:50px;height:50px;background:radial-gradient(circle,#eee 0%,#c7c7c7 35%,#fff 70%)}
.card .img.gold{background:radial-gradient(circle,#f2ecd6 0%,#d1b56a 35%,#fff 70%)}
.card .tag{position:absolute;left:4px;top:4px;width:8px;height:4px;background:var(--gold)}
.card .name{position:absolute;left:4px;top:58px;font-size:3.6px;white-space:nowrap}
.card .desc{position:absolute;left:4px;top:64px;width:50px;font-size:2.8px;line-height:1.3;color:#666}
.card .price{position:absolute;left:4px;top:80px;font-size:2.8px;color:#666}
.card .view{position:absolute;left:4px;top:89px;width:20px;height:5px;background:#f2a93b;font-size:2.8px;color:var(--white);display:flex;align-items:center;justify-content:center}
.card .icons{position:absolute;right:6px;top:89px;display:flex;gap:3px}
.card .icons span{width:5px;height:4px;border:1px solid #777}

/* loose diamonds */
.loose{left:0;top:597px;width:290px;height:101px;background:var(--black);color:var(--white);text-align:center}
.loose h2{position:absolute;left:0;right:0;top:16px;font-size:7px;font-weight:400}
.loose p{position:absolute;left:55px;right:55px;top:27px;font-size:4px;line-height:1.3}
.search{left:84px;top:70px;width:130px;height:10px;background:var(--white);font-size:4px;color:#999;text-align:left;padding-left:5px;line-height:10px}
.search svg{position:absolute;right:3px;top:2px}

/* education */
.edu{left:0;top:698px;width:290px;height:112px;background:linear-gradient(90deg,#555 0%,#6b6b6b 50%,#8a8a8a 75%,#5a5a5a 100%)}
.edu h2{position:absolute;left:21px;top:26px;font-size:7px;font-weight:400;color:var(--white)}
.edu p{position:absolute;left:21px;top:38px;width:140px;font-size:4.2px;line-height:1.3;color:#eee}

/* best selling */
.best{position:absolute;top:852px;width:80px;height:78px;border:1px solid #bbb}
.best.grey{background:#8d8d8d;color:#ddd}
.best.ring{background:radial-gradient(circle,#f3efe0 0%,#d3bb72 35%,#fff 68%)}
.best.ring.silver{background:radial-gradient(circle,#f4f4f4 0%,#c4c4c4 38%,#fff 70%)}
.best.grey .t{position:absolute;left:0;right:0;top:14px;text-align:center;font-size:7px;line-height:1.4}

/* drive */
.drive{left:0;top:957px;width:290px;height:89px;background:radial-gradient(ellipse at 55% 55%,#6a6a6a 0%,#3b3b3b 60%,#2e2e2e 100%);color:var(--white);text-align:center}
.drive h2{position:absolute;left:0;right:0;top:22px;font-size:6px;font-weight:700}
.drive p{position:absolute;left:0;right:0;top:34px;font-size:3.4px;color:#ddd}

/* footer */
.foot{left:0;top:1046px;width:290px;height:112px;background:var(--grey-foot);color:var(--white)}
.foot h4{position:absolute;top:24px;font-size:4.4px;font-weight:400;white-space:nowrap}
.foot p{position:absolute;font-size:3.4px;line-height:1.4;color:#eee;white-space:nowrap}
.foot .mail{position:absolute;left:190px;top:40px;width:80px;height:8px;background:var(--white);font-size:3.2px;color:#999;padding-left:3px;line-height:8px}
.foot .rule{position:absolute;left:30px;right:30px;top:96px;height:1px;background:#777}
.foot .copy{position:absolute;left:0;right:0;top:102px;text-align:center;font-size:3.4px}
</style>
</head>
<body>
<div class="page">

  <div class="abs topbar">
    <span>&#9679;</span><span>&#9679;</span><span>&#9679;</span>
    <span>NEED HELP: Call+100555014</span>
    <div class="right"><span>My Account</span><span>Blog</span><span>Company</span><span>Login</span>
      <svg width="6" height="5" viewBox="0 0 6 5"><path d="M0 .5h1.2l1 3h3l.6-2.2H1.6" fill="none" stroke="#111" stroke-width=".6"/></svg>
    </div>
  </div>

  <div class="abs nav">
    <div class="abs logo"><span class="mark"></span><div>QUILLSTONE<small>JEWELLERS</small></div></div>
    <span class="abs menu" style="left:118px">HOME</span>
    <span class="abs menu active" style="left:137px">COLLECTION &#9662;</span>
    <span class="abs menu" style="left:181px">ON SALE</span>
    <span class="abs menu" style="left:211px">EDUCATION</span>
    <span class="abs menu" style="left:254px">CONTACT</span>
  </div>

  <div class="abs hero" role="img" aria-label="Model wearing gold jewellery and a headpiece against a dark backdrop"></div>
  <div class="abs hero-title">Jewellers</div>
  <div class="abs hero-sub">LOREM IPSUM DOLOR SIT AMET, CONSECTETUR<br>ADIPISCING ELIT, SED.</div>
  <div class="btn" style="left:21px;top:113px;width:48px;height:13px">SHOP NOW</div>

  <svg class="abs cut" width="290" height="191" viewBox="0 0 290 191">
    <path d="M0 0 L42 29 L254 29 L254 191 L0 191Z" fill="#fff"/>
    <path d="M254 120 Q270 140 290 125 L290 191 L254 191Z" fill="#fff"/>
  </svg>

  <div class="tile photo" style="left:42px;top:152px" role="img" aria-label="Oval diamond solitaire ring in white gold"></div>
  <div class="tile black" style="left:148px;top:152px">
    <h3>ENGAGEMENT</h3>
    <p>Lorem ipsum dolor sit amet, consectetur adipiscing elit, sed do eiusmod tempor incididunt ut labore.</p>
    <div class="btn" style="left:14px;top:58px;width:26px;height:6px">MORE</div>
  </div>
  <div class="tile black" style="left:42px;top:248px">
    <h3>Jewellery</h3>
    <p>Lorem ipsum dolor sit amet, consectetur adipiscing elit, sed do eiusmod tempor incididunt ut labore.</p>
    <div class="btn" style="left:14px;top:58px;width:26px;height:6px">MORE</div>
  </div>
  <div class="tile photo gold" style="left:148px;top:248px" role="img" aria-label="Diamond halo ring in yellow gold"></div>

  <div class="dropdown abs">
    <div>DIMONDS</div><div class="on">WEDDING</div><div>ENGAGEMENT RING</div><div>JEWELARY</div>
  </div>

  <div class="abs sale">
    <div class="abs gem" role="img" aria-label="Yellow gemstone"></div>
    <h2>SAVE 50% OFF</h2>
    <div class="sub">Shop our Year-End sale - upto 50%</div>
    <div class="btn-outline" style="left:123px;top:62px;width:44px;height:10px">Shop Now</div>
  </div>

  <div class="abs section-h" style="left:36px;top:457px">Featured Product</div>
  <div class="card" style="left:20px"><div class="img" role="img" aria-label="Marquise engagement ring"></div><span class="tag"></span><div class="name">Engagement Ring</div><div class="desc">Lorem ipsum dolor sit amet, consectetur adipiscing elit sed.</div><div class="price">$ 899.00</div><div class="view">VIEW</div><div class="icons"><span></span><span></span></div></div>
  <div class="card" style="left:84px"><div class="img" role="img" aria-label="Diamond wedding ring"></div><div class="name">Wedding Ring</div><div class="desc">Lorem ipsum dolor sit amet, consectetur adipiscing elit sed.</div><div class="price">$ 749.00</div><div class="view">VIEW</div><div class="icons"><span></span><span></span></div></div>
  <div class="card lift" style="left:148px"><div class="img gold" role="img" aria-label="Gold halo ring"></div><div class="name">Gold Ring</div><div class="desc">Lorem ipsum dolor sit amet, consectetur adipiscing elit sed.</div><div class="price">$ 699.00</div><div class="view">VIEW</div><div class="icons"><span></span><span></span></div></div>
  <div class="card" style="left:212px"><div class="img" role="img" aria-label="Oval diamond ring"></div><div class="name">Diamond Ring</div><div class="desc">Lorem ipsum dolor sit amet, consectetur adipiscing elit sed.</div><div class="price">$ 999.00</div><div class="view">VIEW</div><div class="icons"><span></span><span></span></div></div>

  <div class="abs loose">
    <h2>Loose Diamonds</h2>
    <p>Lorem ipsum dolor sit amet, consectetur adipiscing elit, sed do eiusmod tempor incididunt ut labore et dolore magna aliqua.</p>
    <div class="abs search">Search
      <svg width="6" height="6" viewBox="0 0 6 6"><circle cx="2.4" cy="2.4" r="1.7" fill="none" stroke="#111" stroke-width=".7"/><path d="M3.7 3.7L5.5 5.5" stroke="#111" stroke-width=".8"/></svg>
    </div>
  </div>

  <div class="abs edu" role="img" aria-label="Jeweller setting a stone at a workbench">
    <h2>EDUCATION CENTER</h2>
    <p>Our education center contains useful tips on how to buy diamonds, engagement rings, wedding bands, and finding that perfect gift for someone you love.</p>
    <div class="btn" style="left:148px;top:67px;width:82px;height:12px">Design your own Ring</div>
  </div>

  <div class="abs section-h" style="left:40px;top:826px">Our Best Selling items</div>
  <div class="best grey" style="left:21px" role="img" aria-label="Diamond ring on sale"><div class="t">Diamond Ring<br>20% off</div><div class="btn" style="left:28px;top:44px;width:24px;height:6px">VIEW</div></div>
  <div class="best ring" style="left:106px" role="img" aria-label="Gold diamond halo ring"></div>
  <div class="best ring silver" style="left:190px" role="img" aria-label="White gold diamond cluster ring"></div>

  <div class="abs drive" role="img" aria-label="Diamond ring resting on dark stone">
    <h2>DRIVE YOUR OWN DESIGN</h2>
    <p>OFFERING VARIOUS STYLES AND MULTIPLE FABRIC OPTIONS.</p>
    <div class="btn-outline" style="left:125px;top:47px;width:40px;height:11px;font-size:3.6px">GET STARTED</div>
  </div>

  <div class="abs foot">
    <h4 style="left:28px">About us.</h4>
    <p style="left:28px;top:36px">Lorem ipsum dolor sit amet,<br>Lorem ipsum dolor sit amet,<br>ipsum dolor sit amet.</p>
    <h4 style="left:117px">PHONE SUPPORT</h4>
    <p style="left:126px;top:36px;text-align:center">24/7 Call us now<br>+10555027</p>
    <h4 style="left:208px">NEWSLETTER</h4>
    <div class="mail">Enter Your Email</div>
    <div class="rule"></div>
    <div class="copy">COPYRIGHT @2018. ALL RIGHT RESERVED.</div>
    <svg class="abs" style="left:274px;top:100px" width="6" height="4" viewBox="0 0 6 4"><path d="M0 4L3 0L6 4Z" fill="#fff"/></svg>
  </div>

</div>
</body>
</html>
```